School District In Need of Powerful Presentation

Create a modern PPT design template -- standard and widescreen -- for the Brisco RE-8K school district inspired by its logo. The presentation should be a modern projection of 21st education that excites the people who view it. The school district is located in a rural farming community with a view of the rocky mountains to its west (check out this picture www.tentstopatmarlowbend.com/AnimatedImages/HomeGallery/000MountainScene.jpg). People in this community want quality education for their children with opportunities for them to be successful after they graduate.

Target Market(s)

The Ardenvale and Toller communities in Northern Colorado

Industry/Entity Type

Education

Font styles to use
Sans Serif

Colors
ec1f27
3176b5
acd036
fece3e
f78f20

Requirements
Must have
• The name of the school district:
• Brisco County School District RE-8K Ardenvale-Toller
• Website address: www.briscore8k.k12.zq.us/
• Email: listen@briscore8k.org
Nice to have
• A couple of color options including their current color scheme: red, gold, black
• Placeholder for pictures of students and teachers
Should not have
• Please do not use the full logo in it's current for, but you may use elements of the logo.

```html
<!DOCTYPE html>
<html lang="en">
<head>
<meta charset="utf-8">
<title>Brisco RE-8K Presentation Template</title>
<link href="https://fonts.googleapis.com/css2?family=Carlito:wght@400;700&display=swap" rel="stylesheet">
<style>
:root{
  --red:#b3121a;
  --red-dark:#7d0a10;
  --red-soft:#c9414b;
  --pink:#f6dadd;
  --ink:#222;
  --grey:#5a5a5a;
  --grey-light:#9a9a9a;
  --gold:#f3e3a2;
  --black:#111;
  --paper:#fff;
}
*{margin:0;padding:0;box-sizing:border-box}
html,body{width:1200px;height:907px;overflow:hidden;background:var(--paper)}
body{font-family:"Carlito",sans-serif;color:var(--ink)}
.stage{position:absolute;left:0;top:0;width:1472px;height:1113px;transform:scale(0.81522);transform-origin:0 0}
.slide{position:absolute;width:362px;height:272px;background:var(--paper);overflow:hidden;box-shadow:inset 0 0 0 1px #3a3a3a}
.fill{position:absolute;left:0;top:0;width:362px;height:272px}
.abs{position:absolute}

/* shared content-slide chrome */
.dash{position:absolute;left:22px;top:17px;width:28px;height:2px;background:linear-gradient(90deg,var(--grey) 50%,var(--red) 50%)}
.title{position:absolute;left:22px;top:23px;font-size:10.5px;font-weight:700;color:var(--ink)}
.subtitle{position:absolute;left:22px;top:40px;font-size:5.5px;color:var(--red)}
.corner{position:absolute;right:0;bottom:10px;width:44px;height:40px;background:var(--pink);clip-path:polygon(100% 0,100% 100%,0 100%)}
.foot{position:absolute;right:0;bottom:0;width:212px;height:11px;background:var(--red);clip-path:polygon(8px 0,100% 0,100% 100%,0 100%);color:#fff;font-size:4.6px;font-weight:700;line-height:11px;padding-left:16px}
.foot .num{position:absolute;right:14px;top:0;font-weight:400}
.mark{position:absolute;display:flex;align-items:center;gap:2px;color:var(--red-dark);font-weight:700;white-space:nowrap}
.mark .dot{border-radius:50%;background:var(--red)}
.mark.small{left:6px;bottom:5px;font-size:5px}
.mark.small .dot{width:9px;height:9px}
.watermark{position:absolute;color:rgba(179,18,26,.09);font-weight:700;white-space:nowrap}
.sketch{position:absolute;background:linear-gradient(180deg,#fff 0%,#efefef 70%,#fff 100%)}
.sketch.faint{background:linear-gradient(180deg,#fff 0%,#f6f1f1 70%,#fff 100%)}

/* cover pieces */
.topbar{position:absolute;left:0;top:0;width:362px;height:8px;background:var(--black)}
.band{position:absolute;left:0;width:362px;background:linear-gradient(90deg,var(--red-dark),var(--red) 50%,var(--red-dark));color:#fff;text-align:center;font-weight:700}
.baseline{position:absolute;left:0;bottom:0;width:362px;height:17px;background:var(--black);color:#fff;font-size:5px;display:flex;justify-content:center;align-items:center;gap:22px}
.baseline span{display:flex;align-items:center;gap:4px}
.baseline i{display:inline-block;width:8px;height:8px;border-radius:50%;background:#fff;box-shadow:inset 0 0 0 2px var(--red)}
.mark.big{font-size:15px}
.mark.big .dot{width:16px;height:16px}

/* bullets */
.bullets{position:absolute;font-size:5.3px;line-height:1.27;list-style:none}
.bullets li{position:relative;padding-left:9px;margin-bottom:5px}
.bullets li::before{content:"";position:absolute;left:1px;top:2px;width:2px;height:2px;border-radius:50%;background:var(--ink)}
.cell{position:absolute;width:162px;height:38px;font-size:5.3px;line-height:1.27;padding:4px 6px 0 16px}
.cell::before{content:"";position:absolute;left:7px;top:6px;width:2px;height:2px;border-radius:50%;background:currentColor}
.cell.hot{background:var(--red-soft);color:#fff}

.section-name{position:absolute;left:22px;font-size:10px;font-weight:700}
.section-dash{position:absolute;left:22px;width:28px;height:2px;background:linear-gradient(90deg,var(--ink) 50%,var(--red) 50%)}
.photo{position:absolute}

/* timeline */
.tl-line{position:absolute;left:24px;top:148px;width:314px;height:6px;border-radius:3px;background:var(--red-soft)}
.tl-node{position:absolute;top:145px;width:12px;height:12px;border-radius:50%;background:#8a8a8a;border:2px solid #fff}
.tl-text{position:absolute;width:66px;text-align:center;font-size:3.4px;line-height:1.25;color:#444}
.tl-text b{display:block;color:var(--red);font-size:4.3px;margin-bottom:2px}
.tl-year{position:absolute;font-size:3.6px;color:var(--red);font-weight:700}

/* people grid */
.frame{position:absolute;width:48px;height:55px;border-radius:4px;border:1px solid #e38f96}
.frame.grey{border-color:#a5a5a5}
.frame-label{position:absolute;width:48px;text-align:center;font-size:4.2px;color:var(--red);font-weight:700}
.frame-label.grey{color:#333}

/* structure */
.step{position:absolute;top:92px;width:56px;height:30px;border-radius:3px;background:#e6e6e6;border:1px solid #9a9a9a;box-shadow:1px 2px 2px rgba(0,0,0,.35);font-size:5px;line-height:1.2;color:#777;display:flex;align-items:center;justify-content:center;text-align:center;padding:2px}
.step.alt{background:#f2e4e5;border-color:#d98f95;color:var(--red-soft)}
.arrow{position:absolute;top:104px;width:0;height:0;border-top:4px solid transparent;border-bottom:4px solid transparent;border-left:6px solid var(--black)}
.sub-step{position:absolute;left:216px;width:58px;border-radius:3px;background:#b1404a;color:#fff;font-size:4.4px;font-weight:700;line-height:1.2;text-align:center;display:flex;align-items:center;justify-content:center;box-shadow:1px 1px 2px rgba(0,0,0,.3)}

/* contact */
.contact-head{position:absolute;font-size:5.6px;font-weight:700}
.contact-row{position:absolute;display:flex;align-items:center;gap:4px;font-size:5.3px;color:#333}
.contact-row i{display:inline-block;width:8px;height:8px;border-radius:50%;background:var(--black)}
.contact-row i.red{background:var(--red)}
</style>
</head>
<body>
<div class="stage">

<!-- 1 cover, grey -->
<section class="slide" style="left:0;top:0">
  <div class="topbar"></div>
  <div class="sketch" style="left:0;top:12px;width:362px;height:80px" role="img" aria-label="Line drawing of a rocky mountain range"></div>
  <div class="mark big" style="left:28px;top:140px"><span class="dot"></span>Brisco RE-8K</div>
  <svg class="fill" viewBox="0 0 362 272">
    <defs><linearGradient id="rg1" x1="0" x2="1"><stop offset="0" stop-color="#d21820"/><stop offset="1" stop-color="#7d0a10"/></linearGradient></defs>
    <polygon points="150,200 168,160 186,200" fill="#6b6b6b"/>
    <polygon points="160,200 198,140 236,200" fill="#3b3b3b"/>
    <polygon points="282,200 325,118 362,190 362,200" fill="#555"/>
    <polygon points="215,200 270,100 325,200" fill="url(#rg1)"/>
  </svg>
  <div class="band" style="top:200px;height:55px;font-size:12px;line-height:17px;padding-top:11px">Brisco County School District RE-8K<br>Ardenvale-Toller</div>
  <div class="baseline"><span><i></i>www.briscore8k.k12.zq.us</span><span><i></i>listen@briscore8k.org</span></div>
</section>

<!-- 2 cover, gold -->
<section class="slide" style="left:369px;top:0">
  <div class="topbar"></div>
  <div class="sketch" style="left:0;top:12px;width:362px;height:80px" role="img" aria-label="Line drawing of a rocky mountain range"></div>
  <div class="mark big" style="left:28px;top:140px"><span class="dot"></span>Brisco RE-8K</div>
  <svg class="fill" viewBox="0 0 362 272">
    <defs><linearGradient id="rg2" x1="0" x2="1"><stop offset="0" stop-color="#d21820"/><stop offset="1" stop-color="#7d0a10"/></linearGradient></defs>
    <polygon points="150,200 172,160 194,200" fill="var(--gold)"/>
    <polygon points="180,200 212,145 244,200" fill="var(--gold)"/>
    <polygon points="215,200 270,100 325,200" fill="url(#rg2)"/>
    <polygon points="282,200 325,118 362,185 362,200" fill="var(--gold)"/>
    <polygon points="282,200 303,160 325,200" fill="#e2b56a"/>
  </svg>
  <div class="band" style="top:200px;height:55px;font-size:12px;line-height:17px;padding-top:11px">Brisco County School District RE-8K<br>Ardenvale-Toller</div>
  <div class="baseline"><span><i></i>www.briscore8k.k12.zq.us</span><span><i></i>listen@briscore8k.org</span></div>
</section>

<!-- 3 cover with photo -->
<section class="slide" style="left:738px;top:0">
  <div class="photo" style="left:0;top:0;width:362px;height:116px;background:linear-gradient(180deg,#9db7d2 0%,#c8d3de 40%,#8a5a44 62%,#6e7a52 100%)" role="img" aria-label="Photo of the elementary school building with its entrance sign"></div>
  <div class="band" style="top:116px;height:36px;font-size:11px;line-height:16px;padding-top:3px">Brisco County School District RE-8K<br>Ardenvale-Toller</div>
  <svg class="fill" viewBox="0 0 362 272">
    <polygon points="0,255 32,205 66,255" fill="var(--gold)"/>
    <polygon points="45,255 88,190 128,255" fill="var(--gold)"/>
    <polygon points="80,255 130,158 180,255" fill="#b3121a"/>
    <polygon points="150,255 190,195 230,255" fill="var(--gold)"/>
    <polygon points="200,255 225,218 250,255" fill="var(--gold)"/>
  </svg>
  <div class="mark" style="left:255px;top:198px;font-size:11px"><span class="dot" style="width:11px;height:11px"></span>Brisco RE-8K</div>
  <div class="baseline"><span><i></i>www.briscore8k.k12.zq.us</span><span><i></i>listen@briscore8k.org</span></div>
</section>

<!-- 4 title slide bullets -->
<section class="slide" style="left:1107px;top:0">
  <div class="dash"></div><div class="title">Title Slide</div><div class="subtitle">Slide subtitle</div>
  <div class="watermark" style="left:105px;top:140px;font-size:34px">Brisco RE-8K</div>
  <ul class="bullets" style="left:28px;top:58px;width:318px">
    <li>Sed ut perspiciatis unde omnis iste natus error sit volup tatem accus antium dolor emque lauda nt ium, totam rem aperiam, eaque ipsa quae ab illo inventore very tatis et quasi architecto beatae vitae dicta sunt explicabo.</li>
    <li>Sed ut perspiciatis unde omnis iste natus error sit volup tatem accus antium dolor emque lauda nt ium, totam rem aperiam, eaque ipsa quae ab illo inventore very tatis et quasi architecto beatae vitae dicta sunt explicabo.</li>
    <li>Sed ut perspiciatis unde omnis iste natus error sit volup tatem accus antium dolor emque lauda nt ium, totam rem aperiam, eaque ipsa quae ab illo inventore very tatis et quasi architecto beatae vitae dicta sunt explicabo.</li>
    <li>Sed ut perspiciatis unde omnis iste natus error sit volup tatem accus antium dolor emque lauda nt ium, totam rem aperiam, eaque ipsa quae ab illo inventore very tatis et quasi architecto beatae vitae dicta sunt explicabo.</li>
    <li>Sed ut perspiciatis unde omnis iste natus error sit volup tatem accus antium dolor emque lauda nt ium, totam rem aperiam, eaque ipsa quae ab illo inventore very tatis et quasi architecto beatae vitae dicta sunt explicabo.</li>
    <li>Sed ut perspiciatis unde omnis iste natus error sit volup tatem accus antium dolor emque lauda nt ium, totam rem aperiam, eaque ipsa quae ab illo inventore very tatis et quasi architecto beatae vitae dicta sunt explicabo.</li>
  </ul>
  <div class="corner"></div><div class="mark small"><span class="dot"></span>Brisco RE-8K</div>
  <div class="foot">© 2017 Brisco County School District RE-8K Ardenvale-Toller<span class="num">4</span></div>
</section>

<!-- 5 two column cells -->
<section class="slide" style="left:0;top:279px">
  <div class="dash"></div><div class="title">Title Slide</div><div class="subtitle">Slide subtitle</div>
  <div class="cell" style="left:22px;top:70px">Sed ut perspiciatis unde omnis iste natus error sit volup tatem accus antium dolor emque lauda nt ium, totam rem aperiam, eaque ipsa quae ab illo inventore very tatis</div>
  <div class="cell hot" style="left:188px;top:70px">Sed ut perspiciatis unde omnis iste natus error sit volup tatem accus antium dolor emque lauda nt ium, totam rem aperiam, eaque ipsa quae ab illo inventore very tatis</div>
  <div class="cell hot" style="left:22px;top:112px">Sed ut perspiciatis unde omnis iste natus error sit volup tatem accus antium dolor emque lauda nt ium, totam rem aperiam, eaque ipsa quae ab illo inventore very tatis</div>
  <div class="cell" style="left:188px;top:112px">Sed ut perspiciatis unde omnis iste natus error sit volup tatem accus antium dolor emque lauda nt ium, totam rem aperiam, eaque ipsa quae ab illo inventore very tatis</div>
  <div class="cell" style="left:22px;top:154px">Sed ut perspiciatis unde omnis iste natus error sit volup tatem accus antium dolor emque lauda nt ium, totam rem aperiam, eaque ipsa quae ab illo inventore very tatis</div>
  <div class="cell hot" style="left:188px;top:154px">Sed ut perspiciatis unde omnis iste natus error sit volup tatem accus antium dolor emque lauda nt ium, totam rem aperiam, eaque ipsa quae ab illo inventore very tatis</div>
  <div class="corner"></div><div class="mark small"><span class="dot"></span>Brisco RE-8K</div>
  <div class="foot">© 2017 Brisco County School District RE-8K Ardenvale-Toller<span class="num">5</span></div>
</section>

<!-- 6 section with farm photo -->
<section class="slide" style="left:369px;top:279px">
  <div class="section-dash" style="top:104px"></div><div class="section-name" style="top:110px">Section slide</div>
  <div class="photo" style="left:155px;top:28px;width:170px;height:226px;background:linear-gradient(180deg,#8fa6c6 0%,#7d8fa8 12%,#5f7a3e 28%,#a4552a 45%,#c98b3e 58%,#8ea248 75%,#b9a160 100%)" role="img" aria-label="Photo of autumn farmland with fields and a barn"></div>
  <div class="corner"></div><div class="mark small"><span class="dot"></span>Brisco RE-8K</div>
  <div class="foot">© 2017 Brisco County School District RE-8K Ardenvale-Toller<span class="num">6</span></div>
</section>

<!-- 7 timeline -->
<section class="slide" style="left:738px;top:279px">
  <div class="dash"></div><div class="title">Time Line</div><div class="subtitle">Time line subtitle</div>
  <div class="watermark" style="left:115px;top:142px;font-size:26px">Brisco RE-8K</div>
  <div class="tl-text" style="left:25px;top:98px"><b>Text</b>Sed ut perspiciatis unde omnis iste natus error sit volup tatem accus antium dolor emque laudant ium, totam rem aperiam</div>
  <div class="tl-text" style="left:148px;top:98px"><b>Text</b>Sed ut perspiciatis unde omnis iste natus error sit volup tatem accus antium dolor emque laudant ium, totam rem aperiam</div>
  <div class="tl-text" style="left:271px;top:98px"><b>Text</b>Sed ut perspiciatis unde omnis iste natus error sit volup tatem accus antium dolor emque laudant ium, totam rem aperiam</div>
  <div class="tl-year" style="left:114px;top:139px">YEAR</div>
  <div class="tl-year" style="left:237px;top:139px">YEAR</div>
  <div class="tl-line"></div>
  <div class="tl-node" style="left:52px"></div>
  <div class="tl-node" style="left:113px"></div>
  <div class="tl-node" style="left:175px"></div>
  <div class="tl-node" style="left:237px"></div>
  <div class="tl-node" style="left:298px"></div>
  <div class="tl-year" style="left:52px;top:162px">YEAR</div>
  <div class="tl-year" style="left:175px;top:162px">YEAR</div>
  <div class="tl-year" style="left:298px;top:162px">YEAR</div>
  <div class="tl-text" style="left:86px;top:178px"><b>Text</b>Sed ut perspiciatis unde omnis iste natus error sit volup tatem accus antium dolor emque laudant ium, totam rem aperiam</div>
  <div class="tl-text" style="left:209px;top:178px"><b>Text</b>Sed ut perspiciatis unde omnis iste natus error sit volup tatem accus antium dolor emque laudant ium, totam rem aperiam</div>
  <div class="corner"></div><div class="mark small"><span class="dot"></span>Brisco RE-8K</div>
  <div class="foot">© 2017 Brisco County School District RE-8K Ardenvale-Toller<span class="num">7</span></div>
</section>

<!-- 8 students -->
<section class="slide" style="left:1107px;top:279px">
  <div class="dash"></div><div class="title">Students Slide</div><div class="subtitle">Slide subtitle</div>
  <div class="frame" style="left:14px;top:68px"></div><div class="frame" style="left:71px;top:68px"></div><div class="frame" style="left:128px;top:68px"></div><div class="frame" style="left:185px;top:68px"></div><div class="frame" style="left:242px;top:68px"></div><div class="frame" style="left:299px;top:68px"></div>
  <div class="frame-label" style="left:14px;top:126px">Student Name</div><div class="frame-label" style="left:71px;top:126px">Student Name</div><div class="frame-label" style="left:128px;top:126px">Student Name</div><div class="frame-label" style="left:185px;top:126px">Student Name</div><div class="frame-label" style="left:242px;top:126px">Student Name</div><div class="frame-label" style="left:299px;top:126px">Student Name</div>
  <div class="frame" style="left:14px;top:152px"></div><div class="frame" style="left:71px;top:152px"></div><div class="frame" style="left:128px;top:152px"></div><div class="frame" style="left:185px;top:152px"></div><div class="frame" style="left:242px;top:152px"></div><div class="frame" style="left:299px;top:152px"></div>
  <div class="frame-label" style="left:14px;top:210px">Student Name</div><div class="frame-label" style="left:71px;top:210px">Student Name</div><div class="frame-label" style="left:128px;top:210px">Student Name</div><div class="frame-label" style="left:185px;top:210px">Student Name</div><div class="frame-label" style="left:242px;top:210px">Student Name</div><div class="frame-label" style="left:299px;top:210px">Student Name</div>
  <div class="corner"></div><div class="mark small"><span class="dot"></span>Brisco RE-8K</div>
  <div class="foot">© 2017 Brisco County School District RE-8K Ardenvale-Toller<span class="num">8</span></div>
</section>

<!-- 9 teachers -->
<section class="slide" style="left:0;top:558px">
  <div class="dash"></div><div class="title">Teachers Slide</div><div class="subtitle">Slide subtitle</div>
  <div class="frame grey" style="left:14px;top:68px"></div><div class="frame grey" style="left:71px;top:68px"></div><div class="frame grey" style="left:128px;top:68px"></div><div class="frame grey" style="left:185px;top:68px"></div><div class="frame grey" style="left:242px;top:68px"></div><div class="frame grey" style="left:299px;top:68px"></div>
  <div class="frame-label grey" style="left:14px;top:126px">Teacher Name</div><div class="frame-label grey" style="left:71px;top:126px">Teacher Name</div><div class="frame-label grey" style="left:128px;top:126px">Teacher Name</div><div class="frame-label grey" style="left:185px;top:126px">Teacher Name</div><div class="frame-label grey" style="left:242px;top:126px">Teacher Name</div><div class="frame-label grey" style="left:299px;top:126px">Teacher Name</div>
  <div class="frame grey" style="left:14px;top:152px"></div><div class="frame grey" style="left:71px;top:152px"></div><div class="frame grey" style="left:128px;top:152px"></div><div class="frame grey" style="left:185px;top:152px"></div><div class="frame grey" style="left:242px;top:152px"></div><div class="frame grey" style="left:299px;top:152px"></div>
  <div class="frame-label grey" style="left:14px;top:210px">Teacher Name</div><div class="frame-label grey" style="left:71px;top:210px">Teacher Name</div><div class="frame-label grey" style="left:128px;top:210px">Teacher Name</div><div class="frame-label grey" style="left:185px;top:210px">Teacher Name</div><div class="frame-label grey" style="left:242px;top:210px">Teacher Name</div><div class="frame-label grey" style="left:299px;top:210px">Teacher Name</div>
  <div class="corner"></div><div class="mark small"><span class="dot"></span>Brisco RE-8K</div>
  <div class="foot">© 2017 Brisco County School District RE-8K Ardenvale-Toller<span class="num">9</span></div>
</section>

<!-- 10 structure -->
<section class="slide" style="left:369px;top:558px">
  <div class="dash"></div><div class="title">Structure Slide</div><div class="subtitle">Slide subtitle</div>
  <div class="step" style="left:28px">Velkommen og siden sidst</div>
  <div class="arrow" style="left:85px"></div>
  <div class="step alt" style="left:92px">Opfølgning på eksamen</div>
  <div class="arrow" style="left:149px"></div>
  <div class="step" style="left:155px">Aktivitetsplanlæg ning og estimering</div>
  <div class="arrow" style="left:212px"></div>
  <div class="step alt" style="left:218px">Ledelse og motivation</div>
  <div class="arrow" style="left:275px"></div>
  <div class="step" style="left:281px">Opsamling af læring</div>
  <div class="sub-step" style="top:132px;height:17px">Lederrollen - ledelse og selvledelse</div>
  <div class="sub-step" style="top:154px;height:17px">Samarbejde på distancen</div>
  <div class="sub-step" style="top:176px;height:11px">Magt og tillid</div>
  <div class="sub-step" style="top:192px;height:17px">Gruppedannelser og Relationer</div>
  <div class="corner"></div><div class="mark small"><span class="dot"></span>Brisco RE-8K</div>
  <div class="foot">© 2017 Brisco County School District RE-8K Ardenvale-Toller<span class="num">10</span></div>
</section>

<!-- 11 section with peaks -->
<section class="slide" style="left:738px;top:558px">
  <div class="sketch faint" style="left:0;top:28px;width:362px;height:56px" role="img" aria-label="Faint line drawing of a mountain range"></div>
  <div class="section-dash" style="top:104px"></div><div class="section-name" style="top:110px">Section&nbsp; Slide</div>
  <svg class="fill" viewBox="0 0 362 272">
    <defs><linearGradient id="rg3" x1="0" x2="1"><stop offset="0" stop-color="#d21820"/><stop offset="1" stop-color="#7d0a10"/></linearGradient></defs>
    <polygon points="180,262 210,218 240,262" fill="var(--gold)"/>
    <polygon points="198,262 235,190 272,262" fill="var(--gold)"/>
    <polygon points="240,262 287,170 334,262" fill="url(#rg3)"/>
    <polygon points="240,262 256,232 272,262" fill="#e2b56a"/>
  </svg>
  <div class="corner"></div><div class="mark small"><span class="dot"></span>Brisco RE-8K</div>
  <div class="foot">© 2017 Brisco County School District RE-8K Ardenvale-Toller<span class="num">11</span></div>
</section>

<!-- 12 two column bullets -->
<section class="slide" style="left:1107px;top:558px">
  <div class="dash"></div><div class="title">Title Slide</div><div class="subtitle">Slide subtitle</div>
  <div class="watermark" style="left:105px;top:140px;font-size:34px">Brisco RE-8K</div>
  <ul class="bullets" style="left:28px;top:58px;width:152px">
    <li>Sed ut perspiciatis unde omnis iste natus error sit volup tatem accus antium dolor emque lauda ntium, totam rem aperiam, eaque ipsa quae ab illo inventore very tatis et quasi architecto beatae vitae dicta sunt explicabo.</li>
    <li>Sed ut perspiciatis unde omnis iste natus error sit volup tatem accus antium dolor emque lauda ntium, totam rem aperiam, eaque ipsa quae ab illo inventore very tatis et quasi architecto beatae vitae dicta sunt explicabo.</li>
    <li>Sed ut perspiciatis unde omnis iste natus error sit volup tatem accus antium dolor emque lauda ntium, totam rem aperiam, eaque ipsa quae ab illo inventore very tatis et quasi architecto beatae vitae dicta sunt explicabo.</li>
  </ul>
  <ul class="bullets" style="left:192px;top:58px;width:152px">
    <li>Sed ut perspiciatis unde omnis iste natus error sit volup tatem accus antium dolor emque lauda ntium, totam rem aperiam, eaque ipsa quae ab illo inventore very tatis et quasi architecto beatae vitae dicta sunt explicabo.</li>
    <li>Sed ut perspiciatis unde omnis iste natus error sit volup tatem accus antium dolor emque lauda ntium, totam rem aperiam, eaque ipsa quae ab illo inventore very tatis et quasi architecto beatae vitae dicta sunt explicabo.</li>
    <li>Sed ut perspiciatis unde omnis iste natus error sit volup tatem accus antium dolor emque lauda ntium, totam rem aperiam, eaque ipsa quae ab illo inventore very tatis et quasi architecto beatae vitae dicta sunt explicabo.</li>
  </ul>
  <div class="corner"></div><div class="mark small"><span class="dot"></span>Brisco RE-8K</div>
  <div class="foot">© 2017 Brisco County School District RE-8K Ardenvale-Toller<span class="num">12</span></div>
</section>

<!-- 13 full picture -->
<section class="slide" style="left:0;top:837px">
  <div class="dash" style="left:22px;top:7px"></div>
  <div class="photo" style="left:20px;top:18px;width:325px;height:216px;background:linear-gradient(180deg,#b9b7ae 0%,#8f8c84 30%,#c5c1b2 45%,#8a9ea4 55%,#7f8a5a 70%,#8f9a4c 85%,#6e7a3e 100%)" role="img" aria-label="Painting of a valley landscape under a cloudy sky"></div>
  <div class="corner"></div><div class="mark small"><span class="dot"></span>Brisco RE-8K</div>
  <div class="foot">© 2017 Brisco County School District RE-8K Ardenvale-Toller<span class="num">13</span></div>
</section>

<!-- 14 section with red block -->
<section class="slide" style="left:369px;top:837px">
  <div class="section-dash" style="top:104px"></div><div class="section-name" style="top:110px">Section slide</div>
  <div class="abs" style="left:155px;top:0;width:170px;height:262px;background:#ad0b12"></div>
  <div class="corner"></div><div class="mark small"><span class="dot"></span>Brisco RE-8K</div>
  <div class="foot">© 2017 Brisco County School District RE-8K Ardenvale-Toller<span class="num">14</span></div>
</section>

<!-- 15 contact -->
<section class="slide" style="left:738px;top:837px">
  <div class="sketch faint" style="left:180px;top:10px;width:182px;height:30px" role="img" aria-label="Faint line drawing of a mountain range"></div>
  <div class="dash"></div><div class="title">Contact Slide</div><div class="subtitle">Slide subtitle</div>
  <div class="contact-head" style="left:55px;top:115px">Contact us:</div>
  <div class="contact-row" style="left:55px;top:128px"><i></i>348, Lorem Avenue, Lorem City, LGA</div>
  <div class="contact-row" style="left:55px;top:147px"><i></i>000 111 222 333 - 555</div>
  <div class="contact-row" style="left:55px;top:166px"><i></i>www.briscore8k.k12.zq.us</div>
  <div class="contact-head" style="left:196px;top:115px;color:var(--red)">Follow us on:</div>
  <div class="contact-row" style="left:196px;top:128px"><i class="red"></i>friendpage.com/loremipsum</div>
  <div class="contact-row" style="left:196px;top:147px"><i class="red"></i>@loremipsum</div>
  <div class="contact-row" style="left:196px;top:166px"><i class="red"></i>www.briscore8k.k12.zq.us</div>
  <div class="corner"></div><div class="mark small"><span class="dot"></span>Brisco RE-8K</div>
  <div class="foot">© 2017 Brisco County School District RE-8K Ardenvale-Toller<span class="num">15</span></div>
</section>

<!-- 16 closing -->
<section class="slide" style="left:1107px;top:837px">
  <div class="topbar"></div>
  <div class="sketch" style="left:0;top:20px;width:362px;height:80px" role="img" aria-label="Line drawing of a rocky mountain range"></div>
  <div class="mark big" style="left:24px;top:140px"><span class="dot"></span>Brisco RE-8K</div>
  <svg class="fill" viewBox="0 0 362 272">
    <defs><linearGradient id="rg4" x1="0" x2="1"><stop offset="0" stop-color="#d21820"/><stop offset="1" stop-color="#7d0a10"/></linearGradient></defs>
    <polygon points="150,200 172,165 194,200" fill="#6b6b6b"/>
    <polygon points="165,200 198,148 231,200" fill="#3b3b3b"/>
    <polygon points="285,200 325,125 362,190 362,200" fill="#555"/>
    <polygon points="210,200 260,110 310,200" fill="url(#rg4)"/>
  </svg>
  <div class="band" style="top:200px;height:72px;font-size:13px;line-height:20px;padding-top:17px;background:linear-gradient(180deg,var(--red) 0%,var(--red-dark) 70%,#2a0305 100%)">THANK YOU FOR YOUR TIME</div>
</section>

</div>
</body>
</html>
```